New Business Card Design Project

2 sided business card required. I have attached some previous designs of items we have had made so you can see the logo etc. we Want the card to look professional and modern. for the final design upload for winning designer please note I need to be able to edit the names / phone numbers on the card design as I need to get them made for different staff.
Updates

extending time so designers can have time to submit

Target Market(s)

new customers

Industry/Entity Type

transport / earthmoving

Contact Information for Business Card

name, phone number email address

Requirements
Nice to have
• professional / impressive looking card (first impressions to customers count)
Should not have
• do not put our mobile number on the design use a generic number

```html
<!DOCTYPE html>
<html lang="en">
<head>
<meta charset="utf-8">
<title>RDK Pty Ltd – Business Card</title>
<link rel="stylesheet" href="https://fonts.googleapis.com/css2?family=Rajdhani:wght@600;700&family=Asap:wght@500;600&display=swap">
<style>
  :root {
    --bg: #2a2a2b;
    --card-black: #0b0b0c;
    --card-dark: #1a1a1c;
    --steel: #c4c7cb;
    --gold-light: #f6dc8a;
    --gold: #d9ac45;
    --gold-deep: #a9782a;
    --ink: #151311;
    --white: #f4f4f4;
  }
  * { box-sizing: border-box; margin: 0; padding: 0; }
  html, body { width: 1200px; height: 900px; overflow: hidden; }
  body { background: var(--bg); position: relative; font-family: "Asap", Arial, sans-serif; }

  .card {
    position: absolute; left: 270px; width: 656px; height: 374px;
    border-radius: 22px; overflow: hidden;
    background: linear-gradient(160deg, #1e1e20 0%, var(--card-black) 60%);
  }
  .card--front { top: 58px; }
  .card--back  { top: 471px; }

  /* photo areas */
  .photo { position: absolute; left: 0; width: 100%; }
  .card--front .photo {
    top: 0; height: 300px;
    background:
      linear-gradient(180deg, rgba(11,11,12,0) 0%, rgba(11,11,12,0) 70%, var(--card-black) 100%),
      linear-gradient(100deg, #141416 0%, #2f3033 30%, #3d3e42 55%, #55575b 75%, #3a3b3e 100%);
  }
  .card--back .photo {
    top: 0; height: 258px;
    background:
      linear-gradient(180deg, rgba(20,20,22,0) 0%, rgba(20,20,22,0) 55%, rgba(150,95,55,0.85) 82%, #b37a4c 100%),
      linear-gradient(100deg, #0f0f10 0%, #242427 35%, #3a3b3e 65%, #2a2a2d 100%);
  }

  /* brand */
  .brand {
    position: absolute; left: 0; width: 100%;
    text-align: center; color: var(--steel);
    font-family: "Rajdhani", Arial, sans-serif; font-weight: 700;
  }
  .brand__name { font-size: 96px; line-height: 86px; letter-spacing: 16px; padding-left: 16px; display: block; }
  .brand__suffix { font-size: 17px; line-height: 18px; display: block; }
  .card--front .brand { top: 22px; }
  .card--front .brand__suffix { margin-top: 6px; }
  .card--back .brand {
    top: 34px; display: flex; justify-content: center; align-items: flex-end;
  }
  .card--back .brand__name { display: inline-block; }
  .card--back .brand__suffix { display: inline-block; margin: 0 0 10px 4px; }

  /* front details */
  .person { position: absolute; right: 348px; top: 252px; text-align: right; }
  .person__name {
    font-family: "Rajdhani", Arial, sans-serif; font-weight: 700;
    font-size: 28px; line-height: 28px; color: var(--gold); letter-spacing: 0.5px;
  }
  .person__role { font-size: 17px; color: var(--white); margin-top: 3px; }

  .divider-v { position: absolute; left: 327px; top: 242px; width: 2px; height: 80px; background: var(--gold); }

  .contact { position: absolute; left: 344px; top: 240px; list-style: none; }
  .contact li {
    display: flex; align-items: center; gap: 8px;
    height: 26px; font-size: 19px; color: var(--white);
  }
  .contact svg { width: 20px; height: 20px; flex: none; }

  .address-band {
    position: absolute; left: 0; bottom: 0; width: 100%; height: 32px;
    background: linear-gradient(90deg, var(--gold-deep), var(--gold-light) 45%, var(--gold) 70%, var(--gold-deep));
    text-align: center; font-size: 18px; font-weight: 600; line-height: 32px; color: var(--ink);
  }

  /* back services */
  .services-band {
    position: absolute; left: 0; top: 258px; width: 100%; height: 116px;
    background: linear-gradient(90deg, var(--gold-deep), var(--gold-light) 40%, var(--gold) 65%, var(--gold-light) 85%, var(--gold-deep));
  }
  .services-tag {
    position: absolute; left: 220px; top: 242px; width: 215px; height: 36px;
    border-radius: 6px; background: var(--ink);
    font-family: "Rajdhani", Arial, sans-serif; font-weight: 700;
    font-size: 24px; line-height: 36px; letter-spacing: 1.5px;
    text-align: center; color: var(--gold);
  }
  .services { position: absolute; left: 34px; top: 292px; width: 620px; display: flex; }
  .services__col {
    list-style: none; width: 206px;
    font-family: "Rajdhani", Arial, sans-serif; font-weight: 700;
    font-size: 17.5px; line-height: 20px; color: var(--ink);
  }
  .services__col + .services__col { border-left: 2px solid var(--ink); padding-left: 8px; }
  .services__col li::before { content: "• "; }
</style>
</head>
<body>

  <section class="card card--front">
    <div class="photo" role="img" aria-label="Photograph of a black road train tipper truck with three trailers"></div>
    <div class="brand"><span class="brand__name">RDK</span><span class="brand__suffix">Pty Ltd</span></div>

    <div class="person">
      <p class="person__name">DANIEL HARTLEY</p>
      <p class="person__role">Manager</p>
    </div>
    <div class="divider-v"></div>
    <ul class="contact">
      <li>
        <svg viewBox="0 0 20 20"><circle cx="10" cy="10" r="9" fill="#d9ac45"/><path d="M7 5.5l1.8 2.2-1 1.2c.7 1.5 1.8 2.6 3.3 3.3l1.2-1 2.2 1.8-1 1.5c-3.5-.3-6.7-3.5-7-7z" fill="#151311"/></svg>
        123-456-2100
      </li>
      <li>
        <svg viewBox="0 0 20 20"><circle cx="10" cy="10" r="9" fill="#d9ac45"/><rect x="5" y="6.5" width="10" height="7" fill="#151311"/><path d="M5 6.5l5 4 5-4" stroke="#d9ac45" stroke-width="1" fill="none"/></svg>
        youremail@example.com
      </li>
      <li>
        <svg viewBox="0 0 20 20"><circle cx="10" cy="10" r="9" fill="#d9ac45"/><circle cx="10" cy="10" r="5" fill="none" stroke="#151311" stroke-width="1.4"/><path d="M5 10h10M10 5c-2 3-2 7 0 10M10 5c2 3 2 7 0 10" stroke="#151311" stroke-width="1" fill="none"/></svg>
        www.yourwebsite.com
      </li>
    </ul>
    <div class="address-band">Your address, city, state, ZIP 0000</div>
  </section>

  <section class="card card--back">
    <div class="photo" role="img" aria-label="Photograph of a road train tipper truck on a red dirt outback road"></div>
    <div class="brand"><span class="brand__name">RDK</span><span class="brand__suffix">Pty Ltd</span></div>

    <div class="services-band"></div>
    <div class="services-tag">OUR SERVICES</div>
    <div class="services">
      <ul class="services__col"><li>ROAD TRAIN TIPPERS</li><li>ROAD TRAIN TIPPERS</li><li>ROAD TRAIN TIPPERS</li></ul>
      <ul class="services__col"><li>ROAD TRAIN TIPPERS</li><li>ROAD TRAIN TIPPERS</li><li>ROAD TRAIN TIPPERS</li></ul>
      <ul class="services__col"><li>ROAD TRAIN TIPPERS</li><li>ROAD TRAIN TIPPERS</li><li>ROAD TRAIN TIPPERS</li></ul>
    </div>
  </section>

</body>
</html>
```